Stationary design for boutique production house

We need a stationary design for our production house, 'Luma Studios' based in Singapore. We produce microfilms as well as podcasts, talkshows and events. Our logo is a stylized icon of our director, who is also the executive producer and host of our programs, Orla. Our main company colors are Red, Black and white. We would like a clean, minimalist design incorporating our existing company logo that conveys a sense of urbanism and elegance.

Logo and font files are attached. f

Target Market(s)

We focus on lifestyle media rather than entertainment.

Industry/Entity Type

Boutique

Font styles to use
Serif
Sans Serif

Colors
ec1f27
ffffff
000000

Requirements
Must have
• Our company logo and at least one of our company colors.
Nice to have
• Our address and contact information.
Should not have
• Changes made to the company logo (using only certain parts of it is fine though)

```html
<!DOCTYPE html>
<html lang="en">
<head>
<meta charset="utf-8">
<title>Luma Studios — Stationery Set</title>
<link rel="stylesheet" href="https://fonts.googleapis.com/css2?family=Bodoni+Moda:wght@400&family=Tinos:wght@400&display=swap">
<style>
  :root{
    --red:#ec1f27;
    --black:#000000;
    --white:#ffffff;
    --ground:#b1b1b1;
    --ink:#222222;
    --flap:#2b2b2b;
  }
  *{box-sizing:border-box;margin:0;padding:0}
  html,body{width:1016px;height:1200px;overflow:hidden}
  body{background:var(--ground);position:relative;font-family:"Tinos",serif;color:var(--ink)}
  .sheet{position:absolute;background:var(--white);box-shadow:0 3px 10px rgba(0,0,0,.18)}
  .edge-bar{position:absolute;left:0;background:var(--black)}

  /* brand name lockup */
  .brand{position:absolute;display:flex;align-items:center;gap:4px;font-family:"Bodoni Moda",serif;font-weight:400;text-transform:uppercase;white-space:nowrap;color:var(--black);letter-spacing:.02em}
  .brand-dot{border-radius:50%;background:var(--red);flex:none}
  .brand--small{font-size:7px}
  .brand--small .brand-dot{width:5px;height:5px}

  /* letterheads */
  .letterhead{width:315px;height:446px}
  .letterhead .edge-bar{width:11px}
  .letterhead--contact{left:102px;top:98px}
  .letterhead--contact .edge-bar{top:46px;height:353px}
  .letterhead--plain{left:443px;top:90px}
  .letterhead--plain .edge-bar{top:46px;height:353px}
  .letterhead .brand{right:10px;top:38px}
  .letterhead-footer{position:absolute;left:10px;bottom:8px;font-size:5.6px;line-height:7.6px}
  .letterhead-footer .address{margin-top:3px}

  /* envelope */
  .envelope-front{left:268px;top:573px;width:313px;height:146px}
  .envelope-front .edge-bar{top:0;width:14px;height:100%}
  .envelope-front .brand{left:22px;top:12px;font-size:5.5px}
  .envelope-front .brand .brand-dot{width:4px;height:4px}
  .envelope-front .return-address{position:absolute;left:22px;top:51px;font-size:4.4px;line-height:5.4px}
  .envelope-back{left:603px;top:573px;width:304px;height:144px;background:linear-gradient(180deg,#ffffff 0%,#ececec 100%)}
  .envelope-back svg{position:absolute;left:0;top:0}

  /* business cards */
  .card{width:186px;height:327px}
  .card-front{left:115px;top:777px}
  .card-front .brand{left:0;right:0;top:120px;justify-content:center;font-size:15px;gap:6px}
  .card-front .brand .brand-dot{width:9px;height:9px}
  .card-rule{position:absolute;left:42px;right:42px;top:153px;height:1px;background:var(--red)}
  .card-name{position:absolute;left:0;right:0;top:168px;text-align:center;color:var(--red);font-size:19px;line-height:22px}
  .card-title{position:absolute;left:0;right:0;top:190px;text-align:center;font-size:13.5px;color:var(--black)}
  .card-address{position:absolute;left:0;right:0;top:213px;text-align:center;font-size:12px;line-height:15.5px;color:var(--black)}
  .card-contact{position:absolute;left:0;right:0;bottom:0;height:62px;background:var(--black);color:var(--white);text-align:center;font-size:12px;line-height:15.5px;padding-top:3px}
  .card-back{left:351px;top:777px;background:var(--red)}
  .card-back .brand{left:0;right:0;top:200px;justify-content:center;color:var(--white);font-size:16px;gap:6px}
  .card-back .brand .brand-dot{width:9px;height:9px;background:var(--white)}

  /* compliments slip */
  .compliments{left:567px;top:862px;width:388px;height:183px}
  .compliments .edge-bar{top:32px;width:12px;height:151px}
  .compliments .brand{left:32px;top:55px;font-size:6.5px}
  .compliments .brand .brand-dot{width:5px;height:5px}
  .compliments-details{position:absolute;left:31px;top:84px;font-size:5.8px;line-height:8.2px}
  .compliments-details .address{margin-top:5px}
  .compliments-greeting{position:absolute;right:14px;top:144px;color:var(--red);font-size:16px}
</style>
</head>
<body>

  <section class="sheet letterhead letterhead--contact" aria-label="Letterhead with contact details">
    <div class="edge-bar"></div>
    <div class="brand brand--small"><span class="brand-dot"></span>Luma Studios</div>
    <div class="letterhead-footer">
      <p>+65 6100 2040</p>
      <p>hello@lumastudios.sg</p>
      <p>www.LumaStudios.com</p>
      <p class="address">404 Lorem Ipsum, Text of the printing, AB&nbsp; 10125</p>
    </div>
  </section>

  <section class="sheet letterhead letterhead--plain" aria-label="Continuation letterhead">
    <div class="edge-bar"></div>
    <div class="brand brand--small"><span class="brand-dot"></span>Luma Studios</div>
  </section>

  <section class="sheet envelope-front" aria-label="Envelope front">
    <div class="edge-bar"></div>
    <div class="brand"><span class="brand-dot"></span>Luma Studios</div>
    <div class="return-address">
      <p>404 Lorem Ipsum</p>
      <p>Text of the printing, AB&nbsp; 10125</p>
    </div>
  </section>

  <section class="sheet envelope-back" aria-label="Envelope back">
    <svg width="304" height="144" viewBox="0 0 304 144">
      <polygon points="0,0 304,0 296,44 8,44" fill="var(--flap)"/>
      <rect x="8" y="114" width="226" height="22" fill="#f7f7f7"/>
    </svg>
  </section>

  <section class="sheet card card-front" aria-label="Business card front">
    <div class="brand"><span class="brand-dot"></span>Luma Studios</div>
    <div class="card-rule"></div>
    <p class="card-name">Your Name</p>
    <p class="card-title">job Title</p>
    <div class="card-address">
      <p>404 Lorem Ipsum</p>
      <p>Text of the printing</p>
      <p>AR&nbsp; 10125</p>
    </div>
    <div class="card-contact">
      <p>+65 6100 2040</p>
      <p>hello@lumastudios.sg</p>
      <p>www.LumaStudios.com</p>
    </div>
  </section>

  <section class="sheet card card-back" aria-label="Business card back">
    <div class="brand"><span class="brand-dot"></span>Luma Studios</div>
  </section>

  <section class="sheet compliments" aria-label="Compliments slip">
    <div class="edge-bar"></div>
    <div class="brand"><span class="brand-dot"></span>Luma Studios</div>
    <div class="compliments-details">
      <p>+65 6100 2040</p>
      <p>hello@lumastudios.sg</p>
      <p>www.LumaStudios.com</p>
      <p class="address">404 Lorem Ipsum</p>
      <p>Text of the printing, AB&nbsp; 10125</p>
    </div>
    <p class="compliments-greeting">With Compliments</p>
  </section>

</body>
</html>
```